Penwick Foot & Ankle Hollisburg Window Vinyl Cling

Hi,
I'm looking to get a window decal done, but need it professionally designed.
-must be 24" x 24"
-Quorum Font
-Include our logo, Podiatry, phone number and website
- The goal is to make this eye catching.
Thank you,
Warren

```html
<!DOCTYPE html>
<html lang="en">
<head>
<meta charset="utf-8">
<title>Penwick Foot &amp; Ankle Hollisburg – Window Cling</title>
<link rel="stylesheet" href="https://fonts.googleapis.com/css2?family=Signika:wght@400;600;700&display=swap">
<style>
  :root {
    --stage: #7a7a7a;
    --paper: #ffffff;
    --orange: #f07838;
    --orange-deep: #e0672a;
    --teal: #4fc1a4;
    --teal-deep: #3ea88e;
    --mist: #e4e4e4;
  }
  html, body {
    margin: 0;
    width: 800px;
    height: 1200px;
    overflow: hidden;
    background: var(--stage);
  }
  .window-cling {
    position: absolute;
    left: 40px;
    top: 240px;
    width: 720px;
    height: 720px;
    box-shadow: 0 8px 18px rgba(0,0,0,.35);
    font-family: "Signika", sans-serif;
  }
  .window-cling svg { display: block; }
  .brand-name { font-weight: 700; fill: var(--orange); }
  .brand-city { font-weight: 700; fill: var(--teal); }
  .logo-name { font-weight: 700; fill: var(--teal); }
  .headline { font-weight: 700; fill: var(--paper); }
  .subline { font-weight: 600; fill: var(--paper); }
  .phone-number { font-weight: 700; fill: var(--paper); }
  .website { font-weight: 700; fill: var(--paper); }
</style>
</head>
<body>
<div class="window-cling">
  <svg width="720" height="720" viewBox="0 0 720 720" xmlns="http://www.w3.org/2000/svg">
    <defs>
      <linearGradient id="teal-band" x1="0" x2="1" y1="0" y2="0">
        <stop offset="0" stop-color="var(--teal-deep)"/>
        <stop offset="1" stop-color="var(--teal)"/>
      </linearGradient>
      <linearGradient id="pill-fill" x1="0" x2="0" y1="0" y2="1">
        <stop offset="0" stop-color="#5fcbb0"/>
        <stop offset="1" stop-color="var(--teal-deep)"/>
      </linearGradient>
      <linearGradient id="photo-tone" x1="0" x2="1" y1="0" y2="1">
        <stop offset="0" stop-color="var(--orange)" stop-opacity="0"/>
        <stop offset="1" stop-color="#b85a2c" stop-opacity=".45"/>
      </linearGradient>
      <filter id="soft-shadow" x="-10%" y="-20%" width="120%" height="160%">
        <feDropShadow dx="0" dy="6" stdDeviation="5" flood-color="#000" flood-opacity=".3"/>
      </filter>
    </defs>

    <!-- background -->
    <rect class="paper" width="720" height="720" fill="var(--paper)"/>

    <!-- logo area -->
    <g class="logo">
      <rect x="24" y="30" width="36" height="36" fill="var(--teal)"/>
      <text class="logo-name" x="70" y="60" font-size="30">PENWICK</text>
    </g>

    <!-- practice name -->
    <text class="brand-name" x="673" y="84" font-size="56" text-anchor="end" textLength="300" lengthAdjust="spacingAndGlyphs">PENWICK</text>
    <text class="brand-name" x="676" y="148" font-size="62" text-anchor="end" textLength="458" lengthAdjust="spacingAndGlyphs">FOOT &amp; ANKLE</text>
    <text class="brand-city" x="678" y="189" font-size="42" text-anchor="end" textLength="288" lengthAdjust="spacingAndGlyphs">HOLLISBURG</text>

    <!-- swoosh bands -->
    <path class="mist-band" d="M0 250 Q200 212 420 222 L720 230 L720 280 Q420 190 0 300 Z" fill="var(--mist)"/>
    <path class="orange-field" d="M0 282 Q330 190 720 272 L720 612 Q380 540 0 612 Z" fill="var(--orange)"/>
    <path class="photo-area" role="img" aria-label="faded photo of a runner's legs climbing steps" d="M470 230 Q620 240 720 272 L720 612 Q600 585 470 578 Z" fill="url(#photo-tone)"/>
    <path class="divider" d="M0 612 Q380 540 720 612 L720 620 Q380 556 0 622 Z" fill="var(--paper)"/>
    <path class="teal-field" d="M0 622 Q380 556 720 620 L720 720 L0 720 Z" fill="url(#teal-band)"/>

    <!-- headline -->
    <text class="headline" x="105" y="382" font-size="128" textLength="525" lengthAdjust="spacingAndGlyphs" filter="url(#soft-shadow)">Podiatry</text>
    <text class="subline" x="106" y="421" font-size="36" textLength="441" lengthAdjust="spacingAndGlyphs">Foor &amp; Ankle Physicians</text>

    <!-- phone button -->
    <g class="phone-button" filter="url(#soft-shadow)">
      <rect x="100" y="452" width="476" height="88" rx="44" fill="var(--paper)"/>
      <rect x="106" y="458" width="464" height="76" rx="38" fill="url(#pill-fill)"/>
    </g>
    <g class="phone-icon" fill="none" stroke="var(--paper)" stroke-width="3.5">
      <circle cx="148" cy="496" r="22"/>
      <path d="M139 483 l6 0 l3 8 l-4 3 q4 8 11 11 l3 -4 l8 3 l0 6 q-2 4 -7 4 q-22 -4 -26 -25 q0 -5 6 -6 z" fill="var(--paper)" stroke="none"/>
    </g>
    <text class="phone-number" x="176" y="516" font-size="56" textLength="368" lengthAdjust="spacingAndGlyphs">(877) 555-0142</text>

    <!-- website -->
    <text class="website" x="360" y="672" font-size="44" text-anchor="middle" textLength="398" lengthAdjust="spacingAndGlyphs">STEPWELLFEET.COM</text>
  </svg>
</div>
</body>
</html>
```